VeloNest Crowdfunding Website 1st Page

I am looking to have a first page created for a new crowd funding website that knocks down the biggest hurdle that creative types and start ups face, legal costs. For creative projects and innovative products, we are providing intellectual property and certain other legal services wrapped into the project costs.

I am using a white label crowdfunding platform that that has a standard look and feel of most crowdfunding sites e.g. tiles with campaigns, listing of campaigns categories, create new campaign options, and donate to campaigns etc. The white label program is branded with the VeloNest logo and colors. At present there is a front page that is just a place holder for someone at ArtHive's great design! What I need is an eye-catching first page that visually and through content optimizes the VeloNest brand. (There should be space for content for those looking to raise money and those looking to donate to campaigns.)

www.pledgewave.example is, of course, the reigning King of crowdfunding. They have been so successful that they no longer have to entice people to launch campaigns there. (So they don't speak as much to those looking to raise money.) Unlike Pledgewave, of the challenges is that I have two customers I need to engage. The first is the potential crowdfund campaign owner who is looking to raise money. The second customer is the donor.

I am looking for a smart page from a marketing standpoint that also grabs you. One should feel the energy of "the crowd" when they look at the page.

Some information regarding the logo: The font is Kabel BK BT. The primary blue is R33, G121, B 159. Hex21799F and the primary greenis R179, G210, B54 Hex B3D236. The third file is a slight variation on the VN logo that you are free to use as well. (Unfortunately, I don't have all the color information for that one readily available.) If you need more files, please just let me know.

Industry/Entity Type

Marketing

Font styles to use
Other font styles liked:
• Kabel Bk BT or complimentary

Requirements
Must have
• Please use the slogan "Where the crowd meets great ideas".

```html
<!DOCTYPE html>
<html lang="en">
<head>
<meta charset="utf-8">
<title>VeloNest — Where the crowd meets great ideas</title>
<link href="https://fonts.googleapis.com/css2?family=Open+Sans:wght@400;600;700&display=swap" rel="stylesheet">
<style>
:root{
  --blue:#21799f;
  --link:#2a8fd0;
  --green:#7cc21e;
  --green-dark:#4f9a12;
  --lime:#b3d236;
  --red:#e8442e;
  --ink:#333;
  --muted:#888;
  --nav:#3a3d40;
  --panel:#f3f3f3;
  --grey:#dedede;
  --line:#d6d6d6;
}
*{box-sizing:border-box;margin:0;padding:0}
html,body{width:684px;height:1200px;overflow:hidden}
body{position:relative;font-family:"Open Sans",Arial,sans-serif;color:var(--ink);
  background:linear-gradient(180deg,#8fb6c6 0,#5eaec0 220px,#3fb6bd 520px,#34b0b6 1000px,#2ea2a8 1200px)}
.abs{position:absolute}
.page{position:absolute;left:97px;top:0;width:491px;height:1200px;background:#fff}
.topnav{left:97px;top:0;width:491px;height:19px;background:var(--nav);font-size:8px;color:#bbb}
.topnav a{position:absolute;top:4px;color:#bbb;text-decoration:none}
.topnav .sep{position:absolute;top:4px;color:#666}
.search{left:368px;top:4px;width:84px;height:11px;background:#e9e9e9;border-radius:3px;font-size:6px;color:#777;padding:1px 7px;white-space:nowrap}
.search-btn{left:457px;top:4px;width:18px;height:12px;background:#6c9de2;border-radius:3px}
.logo-mark{width:30px;height:30px;border-radius:50%;background:var(--blue)}
.logo-name{font-size:16px;line-height:18px;color:var(--blue);font-weight:400;white-space:nowrap}
.slogan{font-size:6px;line-height:8px;color:var(--muted);white-space:nowrap}
.tab-title{font-size:10px;font-weight:700;letter-spacing:.3px}
.tab-sub{font-size:7px;color:#aaa}
.btn-s{height:14px;border-radius:2px;color:#fff;font-size:7.5px;text-align:center;line-height:14px;white-space:nowrap}
.hero{left:97px;top:79px;width:491px;height:198px;background:linear-gradient(100deg,#b9b7b3 0,#a9a8a6 45%,#9b9a98 100%);overflow:hidden}
.hero-art{left:250px;top:0;width:241px;height:198px;background:radial-gradient(circle at 55% 25%,#c9a1d8 0,#e6c46e 22%,#9fb9d0 42%,rgba(150,150,150,0) 70%),radial-gradient(circle at 75% 70%,#7a5e52 0,#8d7b70 28%,rgba(150,150,150,0) 55%)}
.hero h1{font-weight:400;font-size:23px;line-height:28px;color:#fff;white-space:nowrap}
.hero p{font-size:7.5px;line-height:9.5px;color:#fff;width:245px}
.btn-go{height:30px;border-radius:4px;background:linear-gradient(#7ed321,var(--green-dark));color:#fff;font-size:10px;font-weight:600;line-height:30px;padding-left:25px;white-space:nowrap}
.btn-go i{position:absolute;left:7px;top:8px;width:14px;height:14px;border-radius:50%;background:#3d7c0c}
.sidebar{left:117px;top:303px;width:126px;height:202px;background:var(--panel);border:1px solid var(--line);padding:9px 9px}
.sidebar h3{font-size:9px;font-weight:700;white-space:nowrap}
.sidebar p{font-size:6px;color:#999;line-height:8px;margin-top:2px}
.cat-list{list-style:none;margin-top:5px}
.cat-list li{font-size:8px;font-weight:600;color:#555;height:14.4px;padding-left:11px;position:relative}
.cat-list li:before{content:"+";position:absolute;left:0;top:-2px;font-size:11px;color:#999}
.cat-list li.on{color:var(--red)}.cat-list li.on:before{color:var(--red)}
.all-cats{font-size:6.5px;color:var(--red);margin-top:3px}
.section-title{font-size:15px;font-weight:600;color:#333;white-space:nowrap}
.feature{left:270px;top:327px;width:283px;height:176px;border:3px solid #e2e2e2;background:#fff}
.feature-img{left:6px;top:7px;width:134px;height:104px;background:linear-gradient(135deg,#3a6fb0,#c8423a 45%,#e0b84a 75%,#2b4d7a)}
.feature h4{font-size:12px;line-height:14px;font-weight:700;color:var(--link)}
.byline{font-size:5.5px;color:#999;white-space:nowrap}.byline b{color:var(--green-dark)}
.feature p{font-size:6.5px;line-height:8.3px;color:#888}
.stats{left:0;top:126px;width:277px;height:47px;background:var(--panel);border-top:1px solid var(--line)}
.ring{border-radius:50%;border:3px solid var(--lime);background:#fff;text-align:center;color:var(--green-dark);font-weight:700}
.stat-l{font-size:6px;color:#999;text-align:center}
.stat-v{font-size:12px;text-align:center;color:#333}
.popular{left:97px;top:525px;width:491px;height:242px;background:var(--grey)}
.pcard{width:104px;height:188px;background:#fff;border:2px solid #eee;top:37px}
.pcard .thumb{position:absolute;left:0;top:0;width:100px;height:73px}
.thumb.board{background:linear-gradient(135deg,#3a3a3a,#555 50%,#2f2f2f)}
.thumb.portrait{background:radial-gradient(circle at 50% 40%,#777,#3a3a3a 70%)}
.pcard h5{position:absolute;left:5px;top:75px;font-size:7.5px;font-weight:400;color:var(--link);white-space:nowrap}
.pcard .by{position:absolute;left:5px;top:85px;font-size:5px;color:#999}
.pcard p{position:absolute;left:5px;top:95px;width:94px;font-size:5.5px;line-height:7px;color:#999}
.pcard .loc{position:absolute;left:5px;top:132px;font-size:5px;color:#999}
.pcard .foot{position:absolute;left:0;top:141px;width:100px;height:43px;border-top:1px solid #eee}
.pcard .amt{position:absolute;left:5px;top:3px;font-size:10px;font-weight:700;color:var(--link);line-height:10px}
.pcard .lbl{font-size:4.5px;font-weight:700;color:#555;line-height:6px}
.pcard .ring{position:absolute;left:58px;top:2px;width:40px;height:40px;font-size:8px;padding-top:9px;line-height:9px;border-width:4px;border-color:var(--lime) var(--lime) #ddd #ddd}
.ring small{display:block;font-size:4px}
.mosaic{left:113px;top:788px;width:458px;height:172px;
  background:repeating-linear-gradient(90deg,transparent 0 56px,#fff 56px 57px),repeating-linear-gradient(0deg,transparent 0 42px,#fff 42px 43px),linear-gradient(90deg,#c25b4a,#6f9fc7 25%,#c8a46e 50%,#5c8fb8 75%,#b85a4a)}
.discover-box{left:170px;top:831px;width:344px;height:86px;background:#fff}
.discover-box h2{font-size:15px;font-weight:400;color:#444;white-space:nowrap}.discover-box h2 b{color:var(--link);font-weight:700}
.discover-box p{font-size:8.5px;line-height:10px;color:#666;width:205px}
.banner{left:85px;top:984px;width:513px;height:59px;background:#efefef}
.banner h3{font-size:11.5px;font-weight:700;color:#333;white-space:nowrap}
.banner p{font-size:8.5px;line-height:10px;color:#888;width:350px}
.btn-flat{background:linear-gradient(#5fbb2a,#3f8f17);color:#fff;font-size:9px;font-weight:600;text-align:center;border-radius:2px;white-space:nowrap}
.fcol{top:1057px;width:110px;font-size:6px;line-height:9px;color:#777}
.fcol h6{font-size:6.5px;font-weight:700;color:#333;margin-bottom:7px}
.fcol .tw{color:var(--red)}
.fcol em{color:#aaa;font-size:5.5px}
.email-in{border:1px solid #ccc;height:15px;font-size:5.5px;color:#999;padding:3px 4px;margin-top:6px;width:108px}
.links{display:grid;grid-template-columns:58px 50px;white-space:nowrap}
.links .on{color:var(--red)}
.bottom{left:97px;top:1167px;width:491px;height:33px;border-top:1px solid #e5e5e5;background:#fff}
</style>
</head>
<body>
<div class="page"></div>

<nav class="abs topnav">
  <a style="left:20px;color:#fff">Home</a><span class="sep" style="left:45px">|</span>
  <a style="left:65px">About</a><span class="sep" style="left:91px">|</span>
  <a style="left:110px">Help</a><span class="sep" style="left:133px">|</span>
  <a style="left:150px">Contact</a>
</nav>
<div class="abs search">Search Projects</div>
<div class="abs search-btn"></div>

<header>
  <div class="abs logo-mark" style="left:117px;top:32px"></div>
  <div class="abs logo-name" style="left:153px;top:34px">VeloNest</div>
  <div class="abs slogan" style="left:154px;top:53px">Where the crowd meets great ideas</div>
  <div class="abs" style="left:288px;top:37px"><div class="tab-title" style="color:var(--green)">DISCOVER</div><div class="tab-sub">Great Projects</div></div>
  <div class="abs" style="left:350px;top:36px;height:24px;border-left:1px dashed #ccc"></div>
  <div class="abs" style="left:365px;top:37px"><div class="tab-title" style="color:var(--link)">CREATE</div><div class="tab-sub">Your Project</div></div>
  <div class="abs btn-s" style="left:479px;top:39px;width:44px;background:var(--green)">Register</div>
  <div class="abs btn-s" style="left:530px;top:39px;width:39px;background:#5b8fe0">Login</div>
</header>

<section class="abs hero">
  <div class="abs hero-art" role="img" aria-label="Crowd of colourful fragments bursting from a thinking head"></div>
  <h1 class="abs" style="left:10px;top:38px">Need Funds for your<br>Creative Ideas ?</h1>
  <p class="abs" style="left:10px;top:95px">Lorem ipsum dolor sit amet, consectetur adipiscing elit. Donec mattis consequat massa, a rhoncus nunc facilisis vel. Maecenas tristique orci dui. Cum sociis natoque penatibus et magnis dorttitor lacinia sit amet arcu.</p>
  <div class="abs btn-go" style="left:11px;top:144px;width:86px"><i></i>Learn More</div>
</section>

<aside class="abs sidebar">
  <h3>Welcome to VeloNest</h3>
  <p>Donec mattis consequat massa, a rhon cus nunc facilisis vel. Maecenas tristique orci dui.</p>
  <ul class="cat-list">
    <li>Design</li><li>Fashion</li><li>Film</li><li>Games</li><li class="on">Comics</li>
    <li>Design</li><li>Fashion</li><li>Film</li><li>Games</li>
  </ul>
  <div class="all-cats">+ View all categories</div>
</aside>

<h2 class="abs section-title" style="left:270px;top:300px">Staff Picks : <span style="color:var(--red)">Comics</span></h2>
<div class="abs" style="left:475px;top:314px;font-size:6.5px;color:#666;white-space:nowrap">See all <span style="color:var(--red)">18</span> Comic Projects</div>

<article class="abs feature">
  <div class="abs feature-img" role="img" aria-label="Comic book cover art with a team of heroes"></div>
  <div class="abs" style="left:148px;top:5px;width:130px">
    <h4>Vortex Comics Series Special Edition</h4>
    <div class="byline" style="margin-top:3px">by <b>Jonah Reyes</b> in ● London, UK</div>
    <p style="margin-top:8px">Lorem ipsum dolor sit amet, consectetur adipiscing elit. Donec mattis consequat massa, a rhoncus nunc facilisis vel. Maecenas tristique orci dui. Donec mattis consequat massa, a rhoncus nunc facilisis vel. Maecenas tristique orci dui.</p>
  </div>
  <div class="abs stats">
    <div class="abs ring" style="left:13px;top:6px;width:36px;height:36px;font-size:8px;padding-top:9px;line-height:9px">156%<small>FUNDED</small></div>
    <div class="abs" style="left:68px;top:0;height:46px;border-left:1px solid var(--line)"></div>
    <div class="abs" style="left:72px;top:10px;width:60px"><div class="stat-l">BACKERS</div><div class="stat-v">240</div></div>
    <div class="abs" style="left:136px;top:0;height:46px;border-left:1px solid var(--line)"></div>
    <div class="abs" style="left:140px;top:10px;width:68px"><div class="stat-l">PLEDGED</div><div class="stat-v">£15,600</div></div>
    <div class="abs" style="left:211px;top:0;height:46px;border-left:1px solid var(--line)"></div>
    <div class="abs" style="left:214px;top:10px;width:56px"><div class="stat-l">DAYS LEFT</div><div class="stat-v">04</div></div>
  </div>
</article>

<section class="abs popular">
  <h2 class="abs section-title" style="left:17px;top:12px">Popular</h2>
  <div class="abs pcard" style="left:17px"><div class="thumb board" role="img" aria-label="Chalkboard cafe menu"></div><h5>CAFE VERDANT</h5><div class="by">by Cafe Verdant</div><p>Help Cafe Verdant nourish our local community by supporting our Vegetarian Bakery Cafe.</p><div class="loc">● London, UK</div><div class="foot"><div class="amt">£2000<div class="lbl">RAISED</div>18<div class="lbl">DAYS LEFT</div></div><div class="ring">25%<small>FUNDED</small></div></div></div>
  <div class="abs pcard" style="left:135px"><div class="thumb portrait" role="img" aria-label="Black and white portrait photograph"></div><h5>PORTRAITS IV</h5><div class="by">by Lena Marsh</div><p>Bring portrait photography into your living room and support local charities through my studio project.</p><div class="loc">● Surrey, UK</div><div class="foot"><div class="amt">£3456<div class="lbl">RAISED</div>23<div class="lbl">DAYS LEFT</div></div><div class="ring">33%<small>FUNDED</small></div></div></div>
  <div class="abs pcard" style="left:254px"><div class="thumb board" role="img" aria-label="Chalkboard cafe menu"></div><h5>CAFE VERDANT</h5><div class="by">by Cafe Verdant</div><p>Help Cafe Verdant nourish our local community by supporting our Vegetarian Bakery Cafe.</p><div class="loc">● London, UK</div><div class="foot"><div class="amt">£2000<div class="lbl">RAISED</div>18<div class="lbl">DAYS LEFT</div></div><div class="ring">25%<small>FUNDED</small></div></div></div>
  <div class="abs pcard" style="left:372px"><div class="thumb portrait" role="img" aria-label="Black and white portrait photograph"></div><h5>PORTRAITS IV</h5><div class="by">by Lena Marsh</div><p>Bring portrait photography into your living room and support local charities through my studio project.</p><div class="loc">● Surrey, UK</div><div class="foot"><div class="amt">£3456<div class="lbl">RAISED</div>23<div class="lbl">DAYS LEFT</div></div><div class="ring">33%<small>FUNDED</small></div></div></div>
</section>

<div class="abs mosaic" role="img" aria-label="Grid of project photos: paper planes, mountain hikers and sneakers"></div>
<div class="abs discover-box">
  <h2 class="abs" style="left:15px;top:10px"><b>Discover</b> great projects and Support them!</h2>
  <p class="abs" style="left:15px;top:35px">Lum sociis natoque penatibus et magnis dis par rient montes. Dis parturient montes natoque eet magnis dis partu.</p>
  <div class="abs btn-go" style="left:223px;top:34px;width:84px;height:28px;line-height:28px"><i style="top:7px"></i>Learn More</div>
</div>

<section class="abs banner">
  <h3 class="abs" style="left:34px;top:8px">Lorem ipsum dolor sit amet, consectetur adipiscing elit. Donec mattis consequat</h3>
  <p class="abs" style="left:34px;top:22px">Rhoncus nunc facilisis vel. Maecenas tristique orci dui. Cum sociis natoque natibus et magnis dis parturient montes. Cum sociis natoque penatibus et magnis dis arturient montes.</p>
  <div class="abs btn-flat" style="left:387px;top:28px;width:67px;height:22px;line-height:22px">Learn More</div>
</section>

<footer>
  <div class="abs fcol" style="left:117px"><h6>ABOUT</h6>Donec rutrum elit ac arcu bibendum rhoncus in vitae turpis. Quisque fermentum gravida eros non faucibus. Curabitur fermentum, arcu sed cursus commodo.<br><br>sales@velonest.example<br>+1 (555) 555 - 55 - 55</div>
  <div class="abs fcol" style="left:232px"><h6>RECENT TWEETS</h6><span class="tw">@velonest</span> &nbsp; Vivamus porta dui dapibus erat egestas semper. In quis sem neque<br><em>5 minutes ago</em><br><br><span class="tw">@velonest</span> &nbsp; Vivamus porta dui dapibus eras egestas semper. In quis sem neque<br><em>1 day ago</em></div>
  <div class="abs fcol" style="left:348px"><h6>NEWSLETTER SIGNUP</h6>Donec rutrum elit ac arcu bibendum rhoncus in vitae turpis.<div class="email-in">Enter your e-mail address</div><div class="btn-flat" style="width:44px;height:17px;line-height:17px;font-size:6.5px;margin-top:6px">SIGNUP</div></div>
  <div class="abs fcol" style="left:463px"><h6>DISCOVER &amp; CREATE</h6><div class="links"><span>What</span><span>Staff Picks</span><span>Start a project</span><span>Popular</span><span>Project Guidlines</span><span class="on">Recent</span><span>Press</span><span>Small Projects</span><span>Stats</span><span>Most Funded</span></div></div>
  <div class="abs bottom">
    <div class="abs" style="left:20px;top:9px;width:16px;height:16px;border-radius:50%;background:#cfcfcf"></div>
    <div class="abs" style="left:41px;top:10px;font-size:10px;color:#aaa">VeloNest</div>
    <div class="abs" style="right:10px;top:13px;font-size:6.5px;color:#aaa;white-space:nowrap">2013 Copyright <span style="color:var(--link)">VeloNest</span> | All rights reserved.</div>
  </div>
</footer>
</body>
</html>
```